Brambleway Business Card

I have a business that is called "Brambleway Electrical Goods LTD" My company deals with top of the range laptops and mobile phones that are exclusive. I need a business card that will be eye catching but not over complicated.

Target Market(s)

Adults aged 19 to 50
Upper middle class

Industry/Entity Type

Business

Requirements
Must have
• Company name/logo (file attached)
• It must have my contact information which is:

• Name: Dale Margrove

• Position: Managing Director 

• Business Address: 7 Haddon Row, London, W4 9QZ

• Contact Number: 02085519304
• Mobile: 07815206473
• Email: info@brambleway-goods.co.uk
Nice to have
• Simple and stylish
• Eye catching

```html
<!DOCTYPE html>
<html lang="en">
<head>
<meta charset="utf-8">
<title>Brambleway Business Card</title>
<link href="https://fonts.googleapis.com/css2?family=Arimo:wght@400;700&display=swap" rel="stylesheet">
<style>
  :root {
    --page-bg: #e9ecef;
    --blue: #1ea6e0;
    --blue-light: #45bdf0;
    --blue-deep: #128fcc;
    --card-white: #ffffff;
    --card-grey: #d9dfe5;
    --text-dark: #3a3a3a;
    --text-name: #2e2e2e;
    --accent: #1ca8e3;
    --logo-text: #eef7fc;
  }
  * { margin: 0; padding: 0; box-sizing: border-box; }
  html, body {
    width: 1200px;
    height: 974px;
    overflow: hidden;
    background: var(--page-bg);
    font-family: "Arimo", Arial, sans-serif;
  }
  .canvas {
    position: relative;
    width: 1200px;
    height: 974px;
  }
  .business-card {
    position: absolute;
    left: 100px;
    top: 194px;
    width: 1000px;
    height: 586px;
    border-radius: 28px;
    overflow: hidden;
    box-shadow: 0 10px 30px rgba(0, 0, 0, 0.18);
  }
  .card-background {
    position: absolute;
    inset: 0;
    width: 100%;
    height: 100%;
  }
  .brand-name {
    position: absolute;
    left: 86px;
    top: 58px;
    color: var(--logo-text);
    font-weight: 400;
    line-height: 1;
  }
  .brand-name .brand-main {
    display: block;
    font-size: 60px;
    letter-spacing: 2px;
  }
  .brand-name .brand-sub {
    display: block;
    font-size: 27px;
    letter-spacing: 1px;
    margin-top: 8px;
  }
  .contact-person {
    position: absolute;
    left: 67px;
    top: 292px;
    color: var(--text-dark);
  }
  .person-name {
    font-size: 31px;
    font-weight: 700;
    color: var(--text-name);
    line-height: 36px;
  }
  .person-role {
    font-size: 30px;
    line-height: 40px;
  }
  .contact-lines {
    list-style: none;
    margin-top: 42px;
    font-size: 28px;
    line-height: 39px;
  }
  .contact-lines .label {
    display: inline-block;
    width: 62px;
    padding-left: 4px;
  }
  .company-block {
    position: absolute;
    left: 594px;
    top: 280px;
  }
  .company-name {
    color: var(--accent);
    font-size: 28px;
    font-weight: 700;
    line-height: 36px;
  }
  .company-address {
    font-style: normal;
    color: var(--text-dark);
    font-size: 28px;
    line-height: 39px;
    margin-top: 42px;
    padding-left: 11px;
  }
</style>
</head>
<body>
<main class="canvas">
  <section class="business-card">
    <svg class="card-background" viewBox="0 0 1000 586" preserveAspectRatio="none" aria-hidden="true">
      <defs>
        <linearGradient id="cardBase" x1="0" y1="0" x2="1" y2="1">
          <stop offset="0" stop-color="#ffffff"/>
          <stop offset="0.6" stop-color="#eef1f4"/>
          <stop offset="1" stop-color="#d6dde4"/>
        </linearGradient>
        <linearGradient id="blueBand" x1="0" y1="0" x2="1" y2="0.4">
          <stop offset="0" stop-color="#1a9fdc"/>
          <stop offset="0.55" stop-color="#28b0ea"/>
          <stop offset="1" stop-color="#1b9bd6"/>
        </linearGradient>
      </defs>
      <rect class="card-base" width="1000" height="586" fill="url(#cardBase)"/>
      <path class="base-swoosh" d="M0,430 C250,380 520,470 1000,360 L1000,586 L0,586 Z" fill="#ffffff" opacity="0.45"/>
      <path class="blue-wave" d="M0,0 H1000 V135 C850,110 700,118 560,165 C420,212 300,250 0,228 Z" fill="url(#blueBand)"/>
      <path class="wave-highlight" d="M470,0 C560,60 700,90 1000,70 L1000,0 Z" fill="#5cc6f2" opacity="0.35"/>
      <path class="wave-edge" d="M0,228 C300,250 420,212 560,165 C700,118 850,110 1000,135 L1000,150 C850,128 700,136 560,182 C420,228 300,266 0,246 Z" fill="#ffffff" opacity="0.5"/>
    </svg>

    <div class="brand-name">
      <span class="brand-main">BRAMBLEWAY</span>
      <span class="brand-sub">Electrical Goods</span>
    </div>

    <div class="contact-person">
      <p class="person-name">Dale Margrove</p>
      <p class="person-role">Managing Director</p>
      <ul class="contact-lines">
        <li><span class="label">T I</span>02085519304</li>
        <li><span class="label">M I</span>07815206473</li>
        <li><span class="label">E I</span>info@brambleway-goods.co.uk</li>
      </ul>
    </div>

    <div class="company-block">
      <p class="company-name">BRAMBLEWAY<br>Electrical Goods Ltd.</p>
      <address class="company-address">7 Haddon Row,<br>London,<br>W4 9QZ</address>
    </div>
  </section>
</main>
</body>
</html>
```